" Faremos um Guia físico com publicidade de fornecedores do ramos de casamento e um site que além da mesma publicidade para fornecedores terá ainda dicas, informações e brindes para as noivas. "

```html
<!DOCTYPE html>
<html lang="pt-BR">
<head>
<meta charset="UTF-8">
<title>Bellare Noivas – Cartão de Visita</title>
<link href="https://fonts.googleapis.com/css2?family=Montserrat:wght@400;600;700&display=swap" rel="stylesheet">
<style>
  :root {
    --backdrop: #ece7df;
    --card-white: #ffffff;
    --card-black: #0d0d0d;
    --card-black-soft: #222222;
    --gold: #b8913f;
    --gold-light: #e0c27a;
    --gold-deep: #8a6824;
    --ink: #2a2a2a;
    --ink-soft: #555555;
    --photo-light: #f7f5f2;
    --photo-mid: #dcd8d2;
  }
  * { box-sizing: border-box; margin: 0; padding: 0; }
  html, body {
    width: 1200px; height: 1200px; overflow: hidden;
    background: var(--backdrop);
    font-family: "Montserrat", sans-serif;
  }
  .canvas {
    width: 1200px; height: 1200px;
    display: flex; flex-direction: column; align-items: center; justify-content: center;
    gap: 70px;
  }
  .card {
    position: relative;
    width: 900px; height: 514px;
    border-radius: 26px;
    overflow: hidden;
    box-shadow: 0 14px 30px rgba(0,0,0,0.18);
  }
  .card::after {
    content: "";
    position: absolute; left: 0; right: 0; bottom: 0; height: 10px;
    background: linear-gradient(90deg, var(--gold-deep), var(--gold-light), var(--gold));
  }

  /* Front */
  .card--front { background: var(--card-white); }
  .card-photo {
    position: absolute; top: 0; right: 0; width: 52%; height: 100%;
    background: radial-gradient(ellipse at 55% 40%, var(--photo-mid) 0%, var(--photo-light) 55%, var(--card-white) 85%);
  }
  .contact {
    position: absolute; left: 58px; top: 62px;
  }
  .contact-head {
    border-left: 5px solid var(--gold);
    padding-left: 14px;
    margin-bottom: 28px;
  }
  .contact-name {
    color: var(--gold); font-weight: 700; font-size: 30px; letter-spacing: 1px; text-transform: uppercase;
  }
  .contact-role { color: var(--ink); font-weight: 600; font-size: 24px; margin-top: 4px; }
  .contact-list { list-style: none; }
  .contact-item {
    display: flex; align-items: flex-start; gap: 14px;
    color: var(--ink-soft); font-size: 19px; line-height: 1.2; margin-bottom: 14px;
  }
  .contact-icon { flex: 0 0 26px; width: 26px; height: 26px; }
  .front-brand {
    position: absolute; right: 70px; bottom: 90px;
    display: flex; align-items: center; gap: 14px;
  }

  /* Back */
  .card--back {
    background: linear-gradient(160deg, var(--card-black-soft) 0%, var(--card-black) 55%);
    display: flex; align-items: center; justify-content: center;
  }
  .back-brand { display: flex; flex-direction: column; align-items: center; gap: 24px; }

  .brand-mark {
    border-radius: 50%;
    border: 4px solid var(--gold);
  }
  .front-brand .brand-mark { width: 46px; height: 46px; }
  .back-brand .brand-mark { width: 120px; height: 120px; border-width: 6px; }
  .brand-name {
    color: var(--gold); font-weight: 600; text-transform: uppercase; letter-spacing: 4px;
  }
  .front-brand .brand-name { font-size: 34px; }
  .back-brand .brand-name { font-size: 62px; letter-spacing: 8px; }
</style>
</head>
<body>
<main class="canvas">
  <section class="card card--front">
    <div class="card-photo" role="img" aria-label="Fotografia de uma noiva de vestido branco segurando um buquê, em tons claros"></div>
    <div class="contact">
      <div class="contact-head">
        <p class="contact-name">Nome e Sobrenome</p>
        <p class="contact-role">Cargo / Função</p>
      </div>
      <ul class="contact-list">
        <li class="contact-item">
          <svg class="contact-icon" viewBox="0 0 26 26"><circle cx="13" cy="13" r="13" fill="var(--gold)"/><path d="M9 7.5l2.5 0 1 3-1.6 1.2a8 8 0 0 0 3.4 3.4l1.2-1.6 3 1v2.5a1.5 1.5 0 0 1-1.6 1.5A10 10 0 0 1 7.5 9.1 1.5 1.5 0 0 1 9 7.5z" fill="#fff"/></svg>
          <span>(00) 0000-0000</span>
        </li>
        <li class="contact-item">
          <svg class="contact-icon" viewBox="0 0 26 26"><circle cx="13" cy="13" r="13" fill="var(--gold)"/><rect x="7" y="9" width="12" height="8.5" rx="1" fill="#fff"/><path d="M7.5 9.5l5.5 4.5 5.5-4.5" stroke="var(--gold)" stroke-width="1.2" fill="none"/></svg>
          <span>contato@exemplo.com</span>
        </li>
        <li class="contact-item">
          <svg class="contact-icon" viewBox="0 0 26 26"><circle cx="13" cy="13" r="13" fill="var(--gold)"/><circle cx="13" cy="13" r="4" fill="#fff"/></svg>
          <span>social.com/exemplo</span>
        </li>
        <li class="contact-item">
          <svg class="contact-icon" viewBox="0 0 26 26"><circle cx="13" cy="13" r="13" fill="var(--gold)"/><path d="M13 6.5a4.5 4.5 0 0 1 4.5 4.5c0 3.3-4.5 8.5-4.5 8.5s-4.5-5.2-4.5-8.5A4.5 4.5 0 0 1 13 6.5z" fill="#fff"/><circle cx="13" cy="11" r="1.6" fill="var(--gold)"/></svg>
          <span>rua exemplo, sl 000<br>cidade-UF, CEP: 00000-000</span>
        </li>
      </ul>
    </div>
    <div class="front-brand">
      <span class="brand-mark"></span>
      <span class="brand-name">Bellare Noivas</span>
    </div>
  </section>

  <section class="card card--back">
    <div class="back-brand">
      <span class="brand-mark"></span>
      <span class="brand-name">Bellare Noivas</span>
    </div>
  </section>
</main>
</body>
</html>
```